vermalo web design

- Company / Site Description
We are developing a website that will allow anyone in Europe to find in one click, cultural things to do (Exhibition, Museum, Monument, Zoo, Aquarium, Archaeological site…) with friends or family, and to organize the visit (book a ticket / a private visit, book a restaurant nearby…).

Examples
1. You're in London with your girlfriend, it's saturday 10 am, you have two hours to spend and you want to see an exhibition. We provide you in one click all the exhibition matching your location / time and date.

2. You're in Berlin with some friends, it's thursday night you want to go out, but you don't know what to do. We provide you a list of experience, you can select for instance "I want to be on top of the world", and we show you a list of venues matching the selected experience / date / time /location of your request.

- Brand name : Vermalo
- Activity : Cultural Leisure, cultural entertainment

- Target audience
Broad target will be between 20 and 55. Core target will be between 25 and 40. Most likely to live in a city and in Europe.

- Behaviours and preferences
Our user is under time constraint (few minutes to find and choose his visit), idea constraint (is not sure about what to do and see) and money constraint.
He wants to have an easy to use website, not cluttered with information, focussed on added value information. He wants to have a website which is modern, fun and elegant that he will deem as professional and trustworthy.

- Our expectations (Do’s and Don’t)
We want to move away from traditional design. We want some OUT OF THE BOX design. Think of a website design that will look like an app design.
We want to make an awesome / extra ordinary /remember-able design. The design must be so cool, that the user wants to come back to the site. In two words: THINK EXTRAORDINARY.
You can use photos to help the user understand functions. If you use photo, use creative commons license photo.
Avoid black colors

- Functional Requirements
We need Four pages:
1. Home Page (desktop and mobile version): it’s both the homepage and the assistant page. This page will allow the user to find in one click his visit (please refer to the pdf file Assistant home page). The page must be self-explanatory for a first time user.
2. Assistant result page (desktop version): it’s the page that display the results found by the assistant based on the criteria search (please refer to the pdf file mockup - Assistant result page)
3. Site / Event page (desktop version): it’s the page that display each result information (please refer to the pdf file mockup – Event / Site Page)
The pdf files list all the elements include in each page + gives you a mockup of each page (just to put in perspective the element required). You are completely free about the design.
We don’t have the logo yet. Use a dummy logo for your page design.
The selected winner can expect to work with us immediately after the contest and on a on a regular basis later on.

- Technical Requirements
No Flash
For the winner, we will manage the CSS you will just need to provide :
. One PSD file containing all the pages
. Inside the PSD file we want for each page two groups: the first group will embed the desktop design, the second group will embed the responsive mobile design (Home Page only).
In total there should be 4 groups inside the PSD file (3 desktop groups, 1 mobile group).
Each group must contain all the elements specified in the pdf file

Website we like
http://demo.plandorix.example/?theme=Velunt
http://rosabel.quintorhub.example/#home
http://blogsite.fenk.daltoroute.example/2/
http://demo.plandorix.example/?theme=Mosaru
http://www.quarnivo.example/themes/lumbe/
http://gridmarket.example/item/tav-responsive-photography-blog-theme/full_screen_preview/8146027
http://items.zkvortel.example/?product=example
http://uk.harnoway.example

Reason: Due to the request of several designers, we have agreed to add 7 additional days to the contest deadline. Thank you. The vermalo team

Reason: We still need to collect all the votes. Sorry for the delay.

Reason: Hello, We extend the contest deadline, in order to collect all the votes from the poll. We should have everything finalized by sunday. Thank you vermalo team

```html
<!DOCTYPE html>
<html lang="en">
<head>
<meta charset="utf-8">
<title>Vermalo – My Assistant</title>
<link href="https://fonts.googleapis.com/css2?family=Ubuntu:ital,wght@0,300;0,400;0,500;1,400&display=swap" rel="stylesheet">
<style>
  :root {
    --brand-red: #c8393b;
    --header-dark: #2f2f2f;
    --tab-dark: #383434;
    --chip-grey: #aba7a8;
    --text-dark: #1e1e1e;
    --text-muted: #6b6b6b;
    --star-gold: #e9a722;
    --white: #ffffff;
  }
  * { box-sizing: border-box; margin: 0; padding: 0; }
  html, body { width: 1200px; height: 790px; overflow: hidden; background: var(--white); }
  body { position: relative; font-family: "Ubuntu", sans-serif; color: var(--text-dark); }
  .abs { position: absolute; }

  .site-header { position: absolute; left: 0; top: 0; width: 1200px; height: 127px; background: var(--header-dark); }
  .top-tabs { position: absolute; left: 130px; top: 0; width: 940px; height: 12px;
    background: repeating-linear-gradient(90deg, var(--tab-dark) 0 60px, transparent 60px 80px); }
  .brand { position: absolute; left: 131px; top: 22px; font-weight: 300; font-size: 47px; color: var(--brand-red); letter-spacing: -0.5px; }
  .avatar { position: absolute; left: 875px; top: 17px; width: 49px; height: 49px; border: 1px solid #555;
    background: linear-gradient(160deg, #d9d4cc, #8a6d58 60%, #4a3a30); }
  .welcome { position: absolute; left: 936px; top: 38px; font-size: 13px; font-style: italic; color: #bdbdbd; line-height: 16px; }
  .welcome .user { color: var(--brand-red); display: block; }
  .logout { position: absolute; left: 1002px; top: 41px; font-size: 11px; font-weight: 500; color: var(--white); }
  .updown { position: absolute; left: 1060px; top: 40px; }
  .main-nav a { position: absolute; top: 86px; height: 41px; line-height: 41px; font-size: 12px; color: var(--white); text-decoration: none; letter-spacing: 0.3px; }
  .main-nav .active { left: 130px; width: 124px; background: var(--brand-red); text-align: center; }
  .main-nav .fav { left: 280px; }
  .search-btn { position: absolute; left: 1042px; top: 93px; width: 28px; height: 28px; background: #353535; }

  .result-count { position: absolute; left: 130px; top: 188px; font-size: 13px; color: var(--brand-red); }
  .result-count small { font-size: 11px; color: var(--text-dark); margin-left: 4px; }
  .chip { position: absolute; width: 73px; height: 73px; border-radius: 50%; background: var(--chip-grey); color: var(--white);
    font-size: 14px; display: flex; align-items: center; justify-content: center; text-align: center; line-height: 17px; }
  .chip.on { background: var(--brand-red); }
  .map-area { position: absolute; left: 130px; top: 479px; width: 235px; height: 172px;
    background: linear-gradient(135deg, #e6e2da, #d8d4cc 50%, #e9e6df); }

  .section-tag { position: absolute; left: 510px; top: 147px; width: 91px; height: 31px; background: var(--brand-red);
    color: var(--white); font-size: 18px; font-weight: 500; text-align: center; line-height: 31px; }
  .site-card { position: absolute; width: 160px; }
  .site-card .rank { position: absolute; left: -2px; top: -9px; width: 24px; height: 24px; }
  .site-card .rank span { position: absolute; left: 0; top: 5px; width: 24px; text-align: center; font-size: 10px; font-weight: 500; }
  .site-card h3 { position: absolute; left: 29px; top: -1px; font-size: 12px; font-weight: 500; text-transform: uppercase; white-space: nowrap; }
  .site-card .photo { position: absolute; left: 0; top: 21px; width: 128px; height: 152px; }
  .site-card .dist { position: absolute; left: 14px; top: 183px; font-size: 14px; color: var(--brand-red); }
  .site-card .hours { position: absolute; left: -3px; top: 202px; font-size: 13px; display: flex; align-items: center; gap: 4px; }

  .site-footer { position: absolute; left: 0; top: 678px; width: 1200px; height: 49px; background: var(--header-dark); color: var(--white); font-size: 11px; }
  .site-footer .lang-label { position: absolute; left: 130px; top: 21px; }
  .site-footer .lang { position: absolute; left: 211px; top: 21px; }
  .site-footer .lang-arrows { position: absolute; left: 268px; top: 19px; }
  .to-top { position: absolute; left: 1047px; top: 13px; width: 23px; height: 23px; border-radius: 50%; background: #9a9a9a; }
  .legal { position: absolute; left: 0; top: 749px; width: 1200px; text-align: center; font-size: 13px; color: var(--text-muted); }
  .legal .name { color: var(--brand-red); }
</style>
</head>
<body>
  <header class="site-header">
    <div class="top-tabs"></div>
    <div class="brand">Vermalo</div>
    <div class="avatar" role="img" aria-label="Profile photo of the signed-in user"></div>
    <div class="welcome">Welcome<span class="user">Tomas</span></div>
    <div class="logout">LOG OUT</div>
    <svg class="updown" width="11" height="15" viewBox="0 0 11 15"><path d="M1 6 5.5 1 10 6z M1 9 5.5 14 10 9z" fill="#8a8a8a"/></svg>
    <nav class="main-nav">
      <a class="active" href="#">MY ASSISTANT</a>
      <a class="fav" href="#">MY FAVOURITES</a>
    </nav>
    <div class="search-btn">
      <svg width="28" height="28" viewBox="0 0 28 28"><circle cx="11" cy="12" r="4" fill="none" stroke="#8a8a8a" stroke-width="2"/><path d="M14 15 20 21" stroke="#8a8a8a" stroke-width="3"/></svg>
    </div>
  </header>

  <main>
    <p class="result-count">6 SITES ET 1 EXHIBITION <small>MATCH YOUR SELECTION</small></p>
    <div class="chip on" style="left:131px;top:230px">PARIS</div>
    <div class="chip" style="left:211px;top:230px">14 DEC.</div>
    <div class="chip" style="left:292px;top:230px">11.00</div>
    <div class="chip" style="left:131px;top:318px">MEET<br>CELEB.</div>
    <div class="map-area" role="img" aria-label="Street map of central Paris with the selected site pinned and the local weather"></div>

    <div class="section-tag">SITES</div>

    <article class="site-card" style="left:510px;top:200px">
      <svg class="rank" viewBox="0 0 24 24"><path d="M12 1 15 8.5 23 9 17 14.5 19 22.5 12 18 5 22.5 7 14.5 1 9 9 8.5z" fill="var(--star-gold)"/></svg>
      <div class="rank"><span>7</span></div>
      <h3>Musée Belvrin</h3>
      <div class="photo" role="img" aria-label="Photo of the ornate red and gold interior of the wax museum" style="background:linear-gradient(170deg,#5a1e1e,#3a1410 55%,#2a1a14)"></div>
      <p class="dist">Paris – 16 km</p>
      <p class="hours"><svg width="11" height="11" viewBox="0 0 12 12"><circle cx="6" cy="6" r="5" fill="none" stroke="#1e1e1e" stroke-width="1.5"/><path d="M6 3v3h2.5" fill="none" stroke="#1e1e1e" stroke-width="1.3"/></svg>Will close in 8h</p>
    </article>

    <article class="site-card" style="left:724px;top:200px">
      <svg class="rank" viewBox="0 0 24 24"><path d="M12 1 15 8.5 23 9 17 14.5 19 22.5 12 18 5 22.5 7 14.5 1 9 9 8.5z" fill="var(--star-gold)"/></svg>
      <div class="rank"><span>8</span></div>
      <h3>Maison de Ferran…</h3>
      <div class="photo" role="img" aria-label="Photo of a brick townhouse facade over a green square" style="background:linear-gradient(180deg,#7ea6d8 0%,#a9c2de 25%,#8a6550 45%,#6d7f3a 75%,#4f6b2a)"></div>
      <p class="dist">Paris – 16 km</p>
      <p class="hours"><svg width="11" height="11" viewBox="0 0 12 12"><circle cx="6" cy="6" r="5" fill="none" stroke="#1e1e1e" stroke-width="1.5"/><path d="M6 3v3h2.5" fill="none" stroke="#1e1e1e" stroke-width="1.3"/></svg>Will close in 8h</p>
    </article>

    <article class="site-card" style="left:942px;top:200px">
      <svg class="rank" viewBox="0 0 24 24"><path d="M12 1 15 8.5 23 9 17 14.5 19 22.5 12 18 5 22.5 7 14.5 1 9 9 8.5z" fill="var(--star-gold)"/></svg>
      <div class="rank"><span>6</span></div>
      <h3>Cinéfloris</h3>
      <div class="photo" role="img" aria-label="Photo of a modern curved stone film archive building" style="background:linear-gradient(180deg,#d8cdb8,#c9b99c 55%,#5a6670 80%,#3a4048)"></div>
      <p class="dist">Paris – 16 km</p>
      <p class="hours"><svg width="11" height="11" viewBox="0 0 12 12"><circle cx="6" cy="6" r="5" fill="none" stroke="#1e1e1e" stroke-width="1.5"/><path d="M6 3v3h2.5" fill="none" stroke="#1e1e1e" stroke-width="1.3"/></svg>Will close in 8h</p>
    </article>

    <article class="site-card" style="left:510px;top:440px">
      <svg class="rank" viewBox="0 0 24 24"><path d="M12 1 15 8.5 23 9 17 14.5 19 22.5 12 18 5 22.5 7 14.5 1 9 9 8.5z" fill="var(--star-gold)"/></svg>
      <div class="rank"><span>6</span></div>
      <h3>Lucien Orvet …</h3>
      <div class="photo" role="img" aria-label="Photo of a golden costume displayed in a fashion exhibition" style="background:linear-gradient(100deg,#2a1e16,#8a5a2a 40%,#3a2a22 70%,#1a1614)"></div>
      <p class="dist">Paris – 16 km</p>
      <p class="hours"><svg width="11" height="11" viewBox="0 0 12 12"><circle cx="6" cy="6" r="5" fill="none" stroke="#1e1e1e" stroke-width="1.5"/><path d="M6 3v3h2.5" fill="none" stroke="#1e1e1e" stroke-width="1.3"/></svg>Will close in 8h</p>
    </article>
  </main>

  <footer class="site-footer">
    <span class="lang-label">LANGUAGE:</span>
    <span class="lang">ENGLISH</span>
    <svg class="lang-arrows" width="11" height="15" viewBox="0 0 11 15"><path d="M1 6 5.5 1 10 6z M1 9 5.5 14 10 9z" fill="#8a8a8a"/></svg>
    <div class="to-top"><svg width="23" height="23" viewBox="0 0 23 23"><path d="M7 9.5 11.5 14 16 9.5" fill="none" stroke="#2f2f2f" stroke-width="2.5"/></svg></div>
  </footer>
  <p class="legal">Copyright © 2014.<span class="name">Vermalo</span>. All Right Reserved &nbsp; | &nbsp;Privacy Policy</p>
</body>
</html>
```